Re-design my 1-page website to be BETTER!

Hi Guys,
I recently created a 1-page website for market testing purposes for a company I am starting. Problem is, the feedback i've had on the page is its a bit corporate and boring.
I would love you to design something that is fresher, more modern and will generate leads (via the sign up CTA's).
Here is the website as it is now: www.guidelinkhub.com.au.
If you need any info or have questions, just reach out.
Thanks,
Oliver

Target Market(s)

Entrepreneurs

Number of Pages Required

1 page

Font styles to use
Sans Serif

Colors
abd036
34a6d7
ffffff

Requirements
Must have
• Fresh, Modern, high-converting
• I expect 70% of traffic to be mobile so must be mobile optimised first.
Nice to have
• I've highlighted colours i like below, however, I am open to suggestions. I like colours that are gender neutral and show energy and vibrancy.
• I have used Proxima Nova for the fonts, as I find it easy to read however, I am open to suggestions. My main preference is that it displays well and is easily read

```html
<!DOCTYPE html>
<html lang="en">
<head>
<meta charset="utf-8">
<title>GuideLink Hub – A Mentor For Everyone</title>
<link href="https://fonts.googleapis.com/css2?family=Arimo:ital,wght@0,400;0,700;1,400;1,700&display=swap" rel="stylesheet">
<style>
:root{
  --green:#5bcc6c;
  --blue:#2ab4e2;
  --blue-text:#2a9dd6;
  --card-border:#9fd4ee;
  --ink:#3d3d3d;
  --muted:#6a6a6a;
  --light:#f1f1f1;
  --white:#ffffff;
  --faq-a:#bfd0d9;
  --faq-b:#9db4c1;
}
*{box-sizing:border-box;margin:0;padding:0}
html,body{width:1200px;height:4865px;overflow:hidden}
body{font-family:"Arimo",Arial,sans-serif;color:var(--ink);background:var(--white)}
section,header,footer{position:relative;width:1200px;overflow:hidden}
.abs{position:absolute}
.center{left:0;right:0;text-align:center}
.gradient{background:linear-gradient(135deg,var(--green) 0%,var(--blue) 100%)}
.heading{font-style:italic;font-weight:700;color:var(--blue-text)}
.pill{display:inline-block;border-radius:40px;font-weight:700;text-align:center}

/* hero */
.hero{height:580px;color:var(--white)}
.brand{left:22px;top:18px;font-size:34px;font-weight:700}
.nav{right:24px;top:22px;display:flex;gap:34px;font-size:22px;font-weight:700}
.hero-title{top:138px;font-size:58px;font-style:italic;font-weight:700}
.hero-quote{top:222px;left:230px;right:230px;text-align:center;font-size:25px;font-style:italic;line-height:1.3}
.hero-attrib{top:334px;font-size:20px;font-weight:700;font-style:italic}
.hero-btn{top:388px;left:514px;width:172px;height:62px;line-height:58px;border:2px solid var(--white);font-size:20px}
.hero-note{top:496px;font-size:20px}

/* finding */
.finding{height:290px;background:var(--light)}
.finding-photo{left:0;top:0;width:600px;height:290px;background:linear-gradient(120deg,#c9d6e0 0%,#6f8191 55%,#2e3d58 100%)}
.finding-text{left:610px;top:18px;width:575px;text-align:center}
.finding-text h2{font-size:38px;line-height:1.1}
.finding-text p{font-size:12.5px;color:var(--muted);line-height:1.35;margin-top:9px}

/* different */
.different{height:872px;background:#f7f9fa}
.different-photo{left:0;top:0;width:620px;height:872px;background:linear-gradient(90deg,#8d9ba6 0%,#b7c3cc 50%,rgba(247,249,250,0) 100%)}
.different-title{top:50px;font-size:52px}
.different-sub{top:130px;font-size:24px;line-height:1.4;color:var(--ink)}
.step{left:268px;width:686px;height:118px;border:2px solid var(--card-border);border-radius:34px;background:rgba(255,255,255,.72);text-align:center;padding:12px 30px}
.step h3{font-size:27px;color:var(--blue-text);font-weight:700}
.step p{font-size:17px;line-height:1.3;margin-top:6px}
.register{top:790px;left:500px;width:200px;height:62px;line-height:62px;background:var(--blue);color:var(--white);font-size:21px}

/* accelerate */
.accelerate{height:1180px;background:var(--light)}
.accelerate-title{top:88px;font-size:40px;font-style:italic;font-weight:700;color:var(--ink)}
.benefit{width:500px;border:2px solid var(--card-border);border-radius:26px;background:var(--white);text-align:center;padding:30px 40px}
.benefit h3{font-size:34px;color:var(--blue-text);font-weight:700}
.benefit p{font-size:18px;line-height:1.45;color:var(--muted);margin-top:22px}

/* faq */
.faq{height:650px;background:linear-gradient(180deg,var(--faq-a),var(--faq-b))}
.faq-photo{left:600px;top:0;width:600px;height:650px;background:radial-gradient(ellipse at 55% 60%,#f4f4f2 0%,#dfe6e9 35%,rgba(191,208,217,0) 70%)}
.faq-title{top:36px;font-size:44px;font-style:italic;font-weight:700;color:#2f2f2f}
.faq-list{left:90px;top:170px;list-style:none}
.faq-list li{font-size:31px;font-weight:700;color:var(--white);line-height:66px}

/* cta */
.cta{height:600px;color:var(--white)}
.cta-title{top:58px;font-size:52px;font-style:italic;font-weight:700}
.cta-text{top:140px;left:170px;right:170px;text-align:center;font-size:23px;line-height:1.4}
.cta-text p+p{margin-top:22px}
.cta-btn{top:370px;left:500px;width:200px;height:66px;line-height:62px;border:2px solid var(--white);font-size:23px}
.cta-note{top:500px;font-size:21px}

/* contact */
.contact{height:534px;background:var(--white)}
.contact-title{left:40px;top:60px;font-size:54px;font-weight:400;color:#333}
.field{height:40px;border-bottom:1px solid #cfcfcf;font-size:13px;color:#9a9a9a;padding-top:18px}
.submit{left:120px;top:420px;width:320px;height:38px;line-height:38px;font-size:13px;color:var(--white);background:linear-gradient(90deg,var(--green),var(--blue))}
.info{width:270px}
.info h4{font-size:18px;font-weight:700;color:#333}
.info p{font-size:13px;color:var(--muted);line-height:1.5;margin-top:8px}
.info span{display:block;font-size:12px;font-weight:700;color:var(--blue-text);margin-top:6px}

/* footer */
.site-footer{height:159px;color:var(--white)}
.socials{top:44px;left:0;right:0;display:flex;justify-content:center;gap:34px}
.socials span{width:28px;height:28px;border-radius:50%;background:var(--white)}
.copyright{top:104px;font-size:24px}
</style>
</head>
<body>

<header class="hero gradient">
  <div class="abs brand">GuideLink Hub</div>
  <nav class="abs nav"><span>Home</span><span>Services</span><span>Team</span><span>Blog</span><span>Contact</span></nav>
  <h1 class="abs center hero-title">A Mentor For Everyone</h1>
  <p class="abs hero-quote">"We've flipped the model on its head - so now you choose your Mentor. It's never been this easy to get the advice and guidance you need to thrive"</p>
  <p class="abs center hero-attrib">Oliver, Founder - GuideLink Hub</p>
  <a class="abs pill hero-btn">Find my Mentor</a>
  <p class="abs center hero-note">Free Registration, 100% Confidential, 100% Obligation Free</p>
</header>

<section class="finding">
  <div class="abs finding-photo" role="img" aria-label="Photo of a businessman in a suit checking his phone in the city"></div>
  <div class="abs finding-text">
    <h2 class="heading">Finding a Mentor Has<br>Never Been Easier</h2>
    <p>Having a great Mentor will fast-track your personal, professional or business growth. But unless you have an incredible network, finding great Mentors has always been a challenge.</p>
    <p>GuideLink Hub changes all that, levelling the playing field and making it easy for entrepreneurs and professionals to find the advice and guidance they deserve.</p>
    <p>No longer will you have to go searching for your perfect Mentor. We bring the perfect Mentor to you, selected from a global pool of experts, putting the power back in your hands and letting you get on with your growth.</p>
  </div>
</section>

<section class="different">
  <div class="abs different-photo" role="img" aria-label="Photo of a hiker standing on a misty mountain top"></div>
  <h2 class="abs center heading different-title">Mentorship: But Different</h2>
  <p class="abs center different-sub">Finding a Mentor used to be hard, but not any more.<br>We've turned the traditional model on its head, so now Mentors seek you.</p>
  <div class="abs step" style="top:210px"><h3>1. Tell Us What You Need</h3><p>There is no one size fits all approach to Mentorship. So tell us the challenges you are facing and the skill-set your Mentor must have.</p></div>
  <div class="abs step" style="top:372px"><h3>2. Choose Your Mentor</h3><p>Mentors are invited to Mentor you. We select 3 top picks that align with your criteria. It's then up to you whether you choose a Mentor, interview 1 or more or refine your criteria and start again.</p></div>
  <div class="abs step" style="top:534px"><h3>3. Ongoing Support</h3><p>We don't stop once you have your perfect Mentor. We're on hand to make life easy, to keep your sessions on track and provide ongoing support.</p></div>
  <a class="abs pill register">Register for Free</a>
</section>

<section class="accelerate">
  <h2 class="abs center accelerate-title">How a Mentor Will Accelerate Your Growth</h2>
  <div class="abs benefit" style="left:70px;top:180px;height:254px"><h3>1. Impartial advice</h3><p>Imagine being able to speak to someone who has been through the challenges you are currently facing? Who has "been there seen that" and can help you navigate the ups and downs of your career or business?</p></div>
  <div class="abs benefit" style="left:630px;top:180px;height:254px"><h3>2. Avoid the Pitfalls</h3><p>An experienced Mentor will help you see the challenges before they arise and make sure you avoid them altogether. Saving valuable time and money in the process.</p></div>
  <div class="abs benefit" style="left:70px;top:478px;height:262px"><h3>3. A Supportive Ear</h3><p>Running a business and the challenges of everyday life can be extremely stressful. And often, our friends and family just can't get it. So imagine having someone independent who can understand where you're coming from, and help you see things objectively.</p></div>
  <div class="abs benefit" style="left:630px;top:478px;height:262px"><h3>4. Clarity</h3><p>Sometimes we are so caught up in our own world we struggle to see the big picture. Your Mentor will provide an objective, outsider view, helping you to cut through the noise and focus on what's really important.</p></div>
  <div class="abs benefit" style="left:70px;top:780px;height:276px"><h3>5. Motivation</h3><p>Your Mentor has been there before and been in your shoes. They understand what you're going through and will help you to re-focus and re-energise.</p></div>
  <div class="abs benefit" style="left:630px;top:780px;height:276px"><h3>6. Make you Accountable</h3><p>A Mentor is not just there to pick you up - they are to give honest opinions and tell you when you're falling short. Ultimately only you can control your success and your Mentor will hold you accountable to make sure you are.</p></div>
</section>

<section class="faq">
  <div class="abs faq-photo" role="img" aria-label="Photo of a small succulent plant in a white ceramic pot"></div>
  <h2 class="abs center faq-title">Frequently Asked Questions</h2>
  <ul class="abs faq-list">
    <li>What is a Mentor?</li>
    <li>Is a Mentor right for me?</li>
    <li>How often do we meet?</li>
    <li>Can I have more than one Mentor?</li>
    <li>What if it doesn't work out?</li>
    <li>How do we meet?</li>
    <li>What are the costs?</li>
  </ul>
</section>

<section class="cta gradient">
  <h2 class="abs center cta-title">It's Time to Invest in You</h2>
  <div class="abs cta-text">
    <p>If you've come this far you've already taken the most important step: recognising how mentorship can help you; and taking action to find it.</p>
    <p>And now your here, the rest is easy.</p>
    <p>Get started now and let GuideLink Hub do the rest...</p>
  </div>
  <a class="abs pill cta-btn">Let's Do This</a>
  <p class="abs center cta-note">Sign up is free, obligation free and 100% confidential</p>
</section>

<section class="contact">
  <h2 class="abs contact-title">Let's Get In Touch</h2>
  <div class="abs field" style="left:40px;top:150px;width:250px">First Name</div>
  <div class="abs field" style="left:320px;top:150px;width:250px">Last Name</div>
  <div class="abs field" style="left:40px;top:220px;width:250px">Email</div>
  <div class="abs field" style="left:320px;top:220px;width:250px">Phone</div>
  <div class="abs field" style="left:40px;top:290px;width:530px;height:90px">Message</div>
  <a class="abs pill submit">SUBMIT REQUEST</a>
  <div class="abs info" style="left:636px;top:150px"><h4>Our Address</h4><p>14 Harbour Lane, Brookvale<br>NSW 2100, Australia</p><span>GET DIRECTIONS</span></div>
  <div class="abs info" style="left:920px;top:150px"><h4>Our Phone</h4><p>Office: 02 5550 1234<br>Mobile: 0400 555 012</p><span>CALL US</span></div>
  <div class="abs info" style="left:636px;top:300px"><h4>Our Email</h4><p>Team: hello@guidelinkhub.com.au<br>Enquiries: info@guidelinkhub.com.au</p><span>SEND A MESSAGE</span></div>
  <div class="abs info" style="left:920px;top:300px"><h4>Our Support</h4><p>Team: help@guidelinkhub.com.au<br>Live chat: weekdays 9am-5pm</p><span>OPEN A TICKET</span></div>
</section>

<footer class="site-footer gradient">
  <div class="abs socials" aria-label="Social links"><span></span><span></span><span></span><span></span><span></span><span></span></div>
  <p class="abs center copyright">© GuideLink Hub</p>
</footer>

</body>
</html>
```